Banner for a National Dental Conference

We need a banner logo for our next Dental Conference in 2017. Our theme is 'Challenging the Status Quo'.
It must have the words '20 years of oral health therapy in Victoria' and the conference date and venue:
7-8th April 2017
Wattlebrook Shore Lodge, Torquay, Victoria.
It must also feature our association logo as attached.
Please be creative, however, we would like a 'clean' design, not cluttered.
The design is intended for use in the conference program and website.

Target Market(s)

Dental practitioners

Industry/Entity Type

Dental

Requirements
Must have
• As above.

```html
<!DOCTYPE html>
<html lang="en">
<head>
<meta charset="utf-8">
<title>National Dental Conference Banner</title>
<link href="https://fonts.googleapis.com/css2?family=Roboto+Condensed:wght@400;700&family=Roboto:wght@400;500&family=Exo+2:wght@600&display=swap" rel="stylesheet">
<style>
  :root {
    --page-bg: #ece9e4;
    --banner-bg: #ffffff;
    --banner-tint: #eef2f6;
    --purple: #5b2d8e;
    --purple-dark: #4a2378;
    --green: #17805a;
    --green-dark: #0f6a49;
    --ink: #1d1d1d;
    --skin-light: #f1d2c2;
    --skin-mid: #d9a58e;
    --hair: #3a2a22;
  }
  * { margin: 0; padding: 0; box-sizing: border-box; }
  html, body {
    width: 1200px;
    height: 657px;
    overflow: hidden;
    background: var(--page-bg);
  }
  .banner {
    position: absolute;
    left: 50px;
    top: 104px;
    width: 1100px;
    height: 448px;
    background: linear-gradient(180deg, var(--banner-bg) 0%, var(--banner-bg) 55%, var(--banner-tint) 100%);
    overflow: hidden;
    box-shadow: 0 2px 10px rgba(0,0,0,0.12);
  }
  .banner__photo {
    position: absolute;
    right: 0; top: 0;
    width: 560px;
    height: 448px;
    background:
      radial-gradient(ellipse 190px 230px at 66% 52%, var(--skin-light) 0%, var(--skin-mid) 60%, rgba(217,165,142,0) 100%),
      linear-gradient(90deg, rgba(255,255,255,0) 0%, rgba(58,42,34,0.55) 22%, var(--hair) 45%, rgba(58,42,34,0.75) 80%, rgba(255,255,255,0.6) 100%);
    -webkit-mask-image: linear-gradient(90deg, transparent 0%, #000 20%);
    mask-image: linear-gradient(90deg, transparent 0%, #000 20%);
  }
  .association-name {
    position: absolute;
    left: 58px;
    top: 44px;
    font-family: "Roboto", sans-serif;
    font-weight: 400;
    font-size: 92px;
    line-height: 1;
    letter-spacing: 2px;
    color: var(--purple);
  }
  .title-band {
    position: absolute;
    left: 0;
    top: 167px;
    width: 640px;
    height: 58px;
    background: linear-gradient(90deg, var(--purple-dark) 0%, var(--purple) 70%, rgba(91,45,142,0) 100%);
    display: flex;
    align-items: center;
    padding-left: 48px;
  }
  .title-band__text {
    font-family: "Roboto Condensed", sans-serif;
    font-weight: 700;
    font-size: 29px;
    color: #fff;
    letter-spacing: 0.3px;
  }
  .event-date {
    position: absolute;
    left: 44px;
    top: 246px;
    display: flex;
    align-items: baseline;
    gap: 16px;
    line-height: 1.2;
  }
  .event-date__days {
    font-family: "Roboto Condensed", sans-serif;
    font-weight: 700;
    font-size: 48px;
    color: var(--green);
  }
  .event-date__year {
    font-family: "Exo 2", sans-serif;
    font-weight: 600;
    font-size: 48px;
    color: var(--ink);
    letter-spacing: 3px;
  }
  .event-venue {
    position: absolute;
    left: 48px;
    top: 318px;
    font-family: "Roboto", sans-serif;
    font-weight: 500;
    font-size: 20px;
    color: var(--ink);
  }
  .tagline-band {
    position: absolute;
    left: 0;
    top: 368px;
    width: 600px;
    height: 30px;
    background: linear-gradient(90deg, var(--green-dark) 0%, var(--green) 80%, rgba(23,128,90,0.2) 100%);
    display: flex;
    align-items: center;
    padding-left: 48px;
  }
  .tagline-band__text {
    font-family: "Roboto", sans-serif;
    font-size: 17px;
    color: #fff;
    letter-spacing: 0.4px;
  }
</style>
</head>
<body>
  <section class="banner">
    <div class="banner__photo" role="img" aria-label="Photograph of a smiling woman with curly dark hair, hands raised to her cheeks"></div>

    <div class="association-name">CORALTA</div>

    <div class="title-band">
      <span class="title-band__text">NATIONAL DENTAL CONFERENCE</span>
    </div>

    <div class="event-date">
      <span class="event-date__days">7-8th APRIL</span>
      <span class="event-date__year">2017</span>
    </div>

    <p class="event-venue">Wattlebrook Shore Lodge, Torquay, Victoria.</p>

    <div class="tagline-band">
      <span class="tagline-band__text">20 YEARS OF ORAL HEALTH THERAPY IN VICTORIA</span>
    </div>
  </section>
</body>
</html>
```